high-impact, conversion-focused website redesign for the government sector

Objective: To design and develop a high-impact, conversion-focused digital platform that solidifies Harrowgate Lumen Advisors (HLA) as the leading communications and strategy firm for government, defense, and industrial clients. The site must project authority, innovation, and sophisticated precision. See the creative breif for more information

Target Market(s)

Government contractors

Industry/Entity Type

Government, defense, industrials

Coding

Coded - Design and coding required

Number of Pages Required

5+ page

Font styles to use
Other font styles liked:
• See the current website

Requirements
Must have
• See design brief
Nice to have
• See design brief
Should not have
• See design brief

```html
<!DOCTYPE html>
<html lang="en">
<head>
<meta charset="utf-8">
<title>Harrowgate Lumen Advisors</title>
<link rel="stylesheet" href="https://fonts.googleapis.com/css2?family=Work+Sans:wght@400;500&family=Rajdhani:wght@700&display=swap">
<style>
  :root {
    --nav-bg: #d1d8df;
    --navy: #0f2d44;
    --ink: #0f2a40;
    --muted: #4d6377;
    --white: #ffffff;
    --accent-green: #7bc142;
  }
  * { margin: 0; padding: 0; box-sizing: border-box; }
  html, body {
    width: 1200px;
    height: 566px;
    overflow: hidden;
    background: var(--white);
    font-family: "Work Sans", Arial, sans-serif;
  }
  .site-header {
    position: absolute;
    top: 0; left: 0;
    width: 1200px;
    height: 33px;
    background: var(--nav-bg);
    border-bottom: 4px solid var(--navy);
    height: 37px;
  }
  .nav-link {
    position: absolute;
    top: 11px;
    font-size: 8.6px;
    font-weight: 500;
    color: var(--ink);
    text-decoration: none;
    letter-spacing: 0.2px;
  }
  .brand {
    position: absolute;
    left: 596px;
    top: 0;
    width: 31px;
    height: 31px;
    background: var(--white);
    display: flex;
    align-items: center;
    justify-content: center;
    font-size: 6px;
    font-weight: 500;
    color: var(--ink);
  }
  .intro {
    position: absolute;
    top: 37px; left: 0;
    width: 1200px;
    height: 303px;
    border-left: 1px solid var(--accent-green);
    text-align: center;
  }
  .intro-lead {
    position: absolute;
    top: 83px;
    left: 318px;
    width: 586px;
    font-size: 15.4px;
    line-height: 20.5px;
    color: var(--ink);
  }
  .intro-body {
    position: absolute;
    top: 165px;
    left: 326px;
    width: 570px;
    font-size: 11px;
    line-height: 19px;
    color: var(--muted);
  }
  .results {
    position: absolute;
    top: 340px; left: 0;
    width: 1200px;
    height: 226px;
    background: var(--navy);
    text-align: center;
    color: var(--white);
  }
  .results-title {
    position: absolute;
    top: 80px;
    left: 0; width: 1200px;
    font-family: "Rajdhani", "Arial Narrow", sans-serif;
    font-weight: 700;
    font-size: 38.5px;
    line-height: 46px;
  }
  .results-body {
    position: absolute;
    top: 144px;
    left: 358px;
    width: 490px;
    font-size: 12.2px;
    line-height: 18px;
  }
</style>
</head>
<body>
  <header class="site-header">
    <a class="nav-link" style="left:200px" href="#">Home</a>
    <a class="nav-link" style="left:246px" href="#">Advisory Services</a>
    <a class="nav-link" style="left:343px" href="#">About Us</a>
    <div class="brand">HLA</div>
    <a class="nav-link" style="left:933px" href="#">Blog</a>
    <a class="nav-link" style="left:973px" href="#">Contact Us</a>
  </header>

  <section class="intro">
    <p class="intro-lead">We help build the communications, government affairs and marketing strategies and systems your organization needs to grow and protect market share — helping our clients meet their mission objectives.</p>
    <p class="intro-body">Our team of award-winning communications strategists bring deep experience across government, defense, and technology. We build systems, teams, and campaigns that drive outcomes for federal contractors and innovators supporting national security, space, and industrial growth.</p>
  </section>

  <section class="results">
    <h2 class="results-title">Proven Results That Drive Real Growth</h2>
    <p class="results-body">We've helped brands strengthen their digital presence, expand their network, and accelerate opportunities across the defense, space, and government sectors.</p>
  </section>
</body>
</html>
```